Elegant invitation for prestigious fund raising event

Background
The Lanterns of Grace is a very prestigious fund raising event. It is a sit down dinner, gala type evening with a presentation and auction.
There are three of these event being held at venues around western North Carolina. The areas where these are being held all have one thing in common, they are in the Appalachian Mountains and the craft of quilt making. As you will see from the Concept Boards attached why a mountain theme and quilt “design feel” is being used. One very important point - we don’t want this design to look like an actual quilt.

See the concept board on page 4, which we can’t use that is from another artist but is one good interpretation of the idea and one way to stylize the picture with a “quilt” interpretation and feel. We do not want a literal quilt representation but are looking for an artistic way on how best to interpret what the quilt represents - the feel of “stitching together” the different things across our region that make us all unique but yet bind us all as one.

The Brief:
We want to develop an elegant invitation for these events.
We have develop as save the date (attached) and all we want to use of this is the wording “Lanterns of Grace” we do not like the icon above it.
Also attached is the wording for the invitation, along with the new picture we want to use (taken from the inspiration boards)

Size, fold, color and paper:

Around 5x7 inches, but open to any dimension if you have an idea that will work in a totally different size. Ideally try and stick to something that will fit a standard envelope so that we don’t need to make a special envelope

Fold – up to you if it has a fold or not and which way it folds. Our thought is that it will need a fold to keep it up market but open to any suggestions.
We are happy to print this on a textured paper if you have suggestions. It will be professionally digital printed so the paper needs to be suitable for digital printing

Color. The inspiration boards show the color palette. We have started out in the save the dates with the navy with reversed out white but again totally up to you to use anything from that color palette.
Updates

Target Market(s)

Up market, around 50 - 65 years old, many are retired, very wealthy

Industry/Entity Type

Event

Requirements
Must have
• See brief attached
Nice to have
• See brief attached
Should not have
• See brief attached

```html
<!DOCTYPE html>
<html lang="en">
<head>
<meta charset="utf-8">
<title>Lanterns of Grace – Invitation</title>
<link rel="stylesheet" href="https://fonts.googleapis.com/css2?family=Lobster&family=Open+Sans:ital,wght@0,400;0,700;1,400&family=Josefin+Sans:wght@300&display=swap">
<style>
  :root {
    --backdrop: #ecebee;
    --navy: #1f1a4d;
    --white: #ffffff;
    --cream: #f6f1e2;
    --peach: #f3cdb4;
    --rose: #e887b8;
    --magenta: #e0529e;
    --sky-orange: #f0a13a;
    --ridge-blue: #6f7fa8;
    --forest: #3f5a2c;
    --ornament: rgba(255,255,255,0.75);
  }
  * { box-sizing: border-box; margin: 0; padding: 0; }
  html, body {
    width: 976px; height: 1200px; overflow: hidden;
    background: var(--backdrop);
  }
  .stage { position: relative; width: 976px; height: 1200px; }

  /* Folded cover card */
  .cover {
    position: absolute; left: 40px; top: 100px;
    width: 600px; height: 790px; overflow: hidden;
  }
  .cover__sky {
    position: absolute; left: 0; top: 0; width: 100%; height: 378px;
    background: linear-gradient(180deg, var(--magenta) 0%, var(--rose) 32%, var(--peach) 62%, var(--cream) 88%);
  }
  .cover__sender {
    position: absolute; left: 0; right: 0; top: 118px;
    display: flex; justify-content: center; align-items: center; gap: 12px;
    transform: rotate(180deg);
    font-family: "Open Sans", sans-serif; font-weight: 700;
    font-size: 19px; letter-spacing: 1px; text-transform: uppercase;
    color: var(--navy);
  }
  .cover__sender-mark { width: 22px; height: 22px; background: var(--navy); }
  .cover__landscape {
    position: absolute; left: 0; top: 378px; width: 100%; height: 412px;
    background: linear-gradient(180deg, #b7a88c 0%, var(--sky-orange) 18%, var(--ridge-blue) 45%, #5d7a4a 68%, var(--forest) 100%);
  }
  .cover__event {
    position: absolute; left: 160px; top: 506px; width: 260px;
    display: flex; flex-direction: column; align-items: center; gap: 14px;
  }
  .cover__event-mark { width: 56px; height: 56px; border-radius: 50%; background: var(--white); }
  .cover__event-name {
    font-family: "Josefin Sans", sans-serif; font-weight: 300;
    font-size: 30px; line-height: 1.15; letter-spacing: 2px;
    text-transform: uppercase; text-align: center; color: var(--white);
  }

  /* Invitation card */
  .invitation {
    position: absolute; left: 428px; top: 368px;
    width: 504px; height: 720px; overflow: hidden;
    background: linear-gradient(180deg, var(--cream) 0%, var(--cream) 14%, var(--peach) 38%, var(--rose) 62%, var(--magenta) 100%);
    color: var(--navy); text-align: center;
    font-family: "Open Sans", sans-serif;
  }
  .invitation__frame { position: absolute; inset: 0; }
  .invitation__fold {
    position: absolute; left: 24px; right: 24px; top: 360px;
    border-top: 1px dashed rgba(255,255,255,0.8);
  }
  .invitation__title {
    position: absolute; left: 0; right: 0; top: 56px;
    font-family: "Lobster", cursive; font-weight: 400; font-size: 30px;
  }
  .invitation__title span { border-bottom: 2px solid var(--navy); padding-bottom: 2px; }
  .line {
    position: absolute; left: 0; right: 0;
    font-size: 14px; line-height: 20px;
  }
  .line--strong { font-weight: 700; }
  .line--caps { text-transform: uppercase; }
  .line--note { font-style: italic; color: var(--white); font-size: 15px; text-transform: uppercase; }
  .line--fine { font-style: italic; color: var(--white); font-size: 11px; }
  .invitation__ornament {
    position: absolute; left: 182px; top: 654px; width: 140px; height: 14px;
    background: var(--ornament); border-radius: 7px; opacity: 0.6;
  }
</style>
</head>
<body>
<main class="stage">

  <section class="cover">
    <div class="cover__sky"></div>
    <div class="cover__sender">
      <span class="cover__sender-mark"></span>
      <span>Ridgeview Valley Hospital</span>
    </div>
    <div class="cover__landscape" role="img" aria-label="Stylised patchwork view of Appalachian ridges at sunset"></div>
    <div class="cover__event">
      <span class="cover__event-mark"></span>
      <span class="cover__event-name">Lanterns<br>of Grace</span>
    </div>
  </section>

  <section class="invitation">
    <svg class="invitation__frame" width="504" height="720" viewBox="0 0 504 720" aria-hidden="true">
      <path d="M26 12 H478 A14 14 0 0 0 492 26 V694 A14 14 0 0 0 478 708 H26 A14 14 0 0 0 12 694 V26 A14 14 0 0 0 26 12 Z"
            fill="none" stroke="#ffffff" stroke-width="2"/>
    </svg>
    <div class="invitation__fold"></div>

    <h1 class="invitation__title"><span>Invitation</span></h1>
    <p class="line" style="top:136px">You are invited to</p>
    <p class="line line--strong" style="top:172px">The Second Annual</p>
    <p class="line" style="top:208px"><strong>LANTERNS OF GRACE</strong> on the plateau.</p>
    <p class="line" style="top:244px">Please join us for an elegant and entertaining affair</p>
    <p class="line" style="top:280px">benefiting the healthcare in our region.</p>

    <p class="line" style="top:422px">6<sup style="font-size:9px">TH</sup> OF JUNE, 2016</p>
    <p class="line line--strong line--caps" style="top:458px">The Meadow at Laurel Creek Lodge</p>
    <p class="line line--caps" style="top:494px">Beginning at 5:30pm</p>
    <p class="line line--caps" style="top:530px">Valet Parking</p>
    <p class="line line--note" style="top:566px">Cocktail Attire &nbsp;•&nbsp; Valet Parking</p>
    <p class="line line--fine" style="top:600px">All Proceeds From The Night Will Go To Benefit Ridgeview Valley Hospital</p>

    <div class="invitation__ornament" role="img" aria-label="Small decorative flourish"></div>
  </section>

</main>
</body>
</html>
```